Need a book cover for a trilogy compilation

I need a book cover for a compilation of a trilogy. I have the 3 book covers right now, but I need something with some 'pop'. It is a sci-fi novel where people gain the ability to sense the past from the world around them. It has a lot of thriller and suspense aspects as well. I am looking for something to keep the same font with the title and subtitle as the other books. The books in the series are The Ashes of Noon: Book One of the Vellmark Sight Series, The Ashes of Malice: Book Two of the Vellmark Sight Series, and The Ashes of Frost: Book Three of the Vellmark Sight Series.
This compilation with be called The Ashes of Creation: The Complete Vellmark Sight Trilogy

Here is the link to the brindlequay author page: https://www.brindlequay.example/stores/Corwin-Malvade/author/K7XTLM2W9P?ref=dbs_m_mng_rwt_byln&qid=1776387964&sr=8-1&shoppingPortalEnabled=true

Target Market(s)

Sci fi readers

Font styles to use
Other font styles liked:
• Whatever the front font currently is, I think it is Trajan

Requirements
Must have
• Same or similar font for the title and subtitle
Nice to have
• something that draws the reader's attention. Everyone judges a book by its cover.

```html
<!DOCTYPE html>
<html lang="en">
<head>
<meta charset="utf-8">
<title>The Ashes of Creation — Cover</title>
<link rel="stylesheet" href="https://fonts.googleapis.com/css2?family=Cinzel:wght@600;700&family=Cormorant+Garamond:wght@600&family=Roboto:wght@400;700&display=swap">
<style>
  :root {
    --stage: #c9d0d0;
    --night: #0b1230;
    --night-deep: #05071a;
    --ember: #e8741c;
    --flame: #ffb43a;
    --core: #fff6c8;
    --gold-light: #fff1a8;
    --gold: #f2c14a;
    --gold-dark: #b0701a;
    --arc-blue: #7fc8ff;
    --spine-blue: #1d3a8c;
    --panel: rgba(236, 238, 242, 0.86);
    --ink: #1c1c1c;
    --photo-frame: #e0342c;
  }
  * { box-sizing: border-box; margin: 0; padding: 0; }
  html, body { width: 1200px; height: 785px; overflow: hidden; }
  body { background: var(--stage); position: relative; font-family: "Roboto", sans-serif; }

  .gold-text {
    background: linear-gradient(180deg, var(--gold-light) 0%, var(--gold) 45%, var(--gold-dark) 100%);
    -webkit-background-clip: text;
    background-clip: text;
    color: transparent;
  }

  /* Front cover */
  .front-cover {
    position: absolute; left: 671px; top: 0; width: 529px; height: 785px; overflow: hidden;
    background: var(--night-deep);
  }
  .cover-art {
    position: absolute; inset: 0;
    background:
      radial-gradient(circle at 50% 47%, var(--core) 0%, rgba(255, 214, 110, 0.95) 5%, rgba(255, 170, 50, 0.55) 14%, transparent 30%),
      radial-gradient(ellipse 30% 9% at 50% 80%, var(--core) 0%, rgba(255, 190, 70, 0.9) 35%, transparent 100%),
      radial-gradient(ellipse 46% 12% at 50% 85%, rgba(232, 116, 28, 0.85), transparent 100%),
      radial-gradient(ellipse 22% 30% at 96% 68%, rgba(255, 110, 20, 0.85), transparent 100%),
      radial-gradient(ellipse 20% 18% at 8% 62%, rgba(232, 116, 28, 0.6), transparent 100%),
      radial-gradient(ellipse 60% 25% at 50% 38%, rgba(70, 110, 200, 0.35), transparent 100%),
      linear-gradient(180deg, var(--night) 0%, #1a1a40 40%, #3a1a10 78%, #1c0c08 92%, var(--night-deep) 100%);
  }
  .time-streams { position: absolute; inset: 0; width: 529px; height: 785px; }
  .vignette {
    position: absolute; inset: 0;
    background: radial-gradient(ellipse 75% 70% at 50% 52%, transparent 55%, rgba(3, 4, 14, 0.7) 100%);
  }
  .cover-title {
    position: absolute; left: 0; right: 0; top: 26px; text-align: center;
    font-family: "Cinzel", serif; font-weight: 700; line-height: 0.98;
    filter: drop-shadow(0 2px 3px rgba(0,0,0,0.75));
  }
  .cover-title .title-the { display: block; font-size: 40px; }
  .cover-title .title-line { display: block; font-size: 66px; }
  .cover-subtitle {
    position: absolute; left: 0; right: 0; top: 194px; text-align: center;
    font-family: "Cormorant Garamond", serif; font-weight: 600; font-size: 23px;
    color: var(--gold-light); text-shadow: 0 1px 3px rgba(0,0,0,0.9);
  }
  .cover-author {
    position: absolute; left: 0; right: 0; top: 712px; text-align: center;
    font-family: "Cinzel", serif; font-weight: 700; font-size: 41px; letter-spacing: 0.5px;
    filter: drop-shadow(0 2px 3px rgba(0,0,0,0.85));
  }

  /* Back cover and spine */
  .print-spread {
    position: absolute; left: 175px; top: 170px; width: 322px; height: 444px; display: flex;
  }
  .back-cover { position: relative; width: 300px; height: 444px; overflow: hidden; }
  .back-art {
    position: absolute; inset: 0;
    background:
      radial-gradient(ellipse 50% 25% at 70% 90%, rgba(232, 116, 28, 0.7), transparent 100%),
      radial-gradient(ellipse 40% 20% at 15% 35%, rgba(232, 116, 28, 0.45), transparent 100%),
      linear-gradient(180deg, #2a2c3a 0%, #3a3440 40%, #3a2418 80%, #1a0e0a 100%);
  }
  .author-panel {
    position: absolute; left: 17px; top: 92px; width: 250px; height: 275px;
    background: var(--panel); border-radius: 12px; padding: 26px 16px 14px; color: var(--ink);
  }
  .author-panel h2 {
    font-size: 7.5px; font-weight: 700; text-align: center; letter-spacing: 0.3px;
    padding-bottom: 6px; border-bottom: 1px solid var(--ink); margin-bottom: 16px;
  }
  .author-intro { display: flex; gap: 6px; margin-bottom: 8px; }
  .author-photo {
    flex: 0 0 40px; height: 44px; background: #fff; border: 2px solid var(--photo-frame); border-radius: 3px;
  }
  .author-panel p { font-size: 5.6px; line-height: 1.45; text-align: justify; }
  .author-panel .note { text-indent: 20px; margin-bottom: 8px; }
  .spine {
    width: 22px; height: 444px; background: linear-gradient(90deg, #16307a, var(--spine-blue), #16307a);
    display: flex; align-items: center; justify-content: flex-start; padding-top: 12px;
    writing-mode: vertical-rl;
    font-family: "Cinzel", serif; font-weight: 700; font-size: 10.5px; color: var(--gold); letter-spacing: 0.5px;
  }
  .spine .spine-author { font-size: 7px; margin-top: 10px; }
</style>
</head>
<body>

  <div class="print-spread">
    <section class="back-cover">
      <div class="back-art" role="img" aria-label="Stormy smoke-filled sky over a burning night city, continuing the front cover artwork"></div>
      <div class="author-panel">
        <h2>ABOUT THE AUTHOR</h2>
        <div class="author-intro">
          <div class="author-photo"></div>
          <p>"Corwin Malvade is the Harbor Ledger bestselling author of Hollow Meridian, the first book in a trilogy that she began writing while still a college student. Now a full-time writer, Ms. Halvey and her husband call the Chicago area home. You can visit her online at www.orlahalveybooks.example or on Pinwire</p>
        </div>
        <p class="note">Why it works: Is this the flashiest bio in the world? Of course not. But that's exactly why it works. Each word builds on the last, adding new information to her story: her name, her qualifications, her books, their history, her home life, and, finally, her online presence. It's short and simple but then again, a bestselling author can afford to be.</p>
        <p class="note">Why it works: Is this the flashiest bio in the world? Of course not. But that's exactly why it works. Each word builds on the last, adding new information to her story: her name, her qualifications, her books, their history, her home life, and, finally, her online presence. It's short and simple but then again, a bestselling author can afford to be.</p>
      </div>
    </section>
    <div class="spine">
      <span class="spine-title">THE ASHES OF CREATION</span>
      <span class="spine-author">— CORWIN MALVADE —</span>
    </div>
  </div>

  <section class="front-cover">
    <div class="cover-art" role="img" aria-label="Cosmic fiery illustration: swirling glowing time streams around ancient monuments and a radiant head, above a figure with outstretched arms standing on an open book before a burning city"></div>
    <svg class="time-streams" viewBox="0 0 529 785" aria-hidden="true">
      <defs>
        <linearGradient id="stream-warm" x1="0" y1="0" x2="1" y2="0">
          <stop offset="0" stop-color="var(--arc-blue)" stop-opacity="0.2"/>
          <stop offset="0.5" stop-color="var(--flame)" stop-opacity="0.95"/>
          <stop offset="1" stop-color="var(--arc-blue)" stop-opacity="0.3"/>
        </linearGradient>
        <filter id="stream-glow" x="-20%" y="-20%" width="140%" height="140%">
          <feGaussianBlur stdDeviation="2.5"/>
        </filter>
      </defs>
      <g fill="none" stroke="url(#stream-warm)" filter="url(#stream-glow)">
        <ellipse cx="264" cy="300" rx="230" ry="60" stroke-width="4" transform="rotate(-8 264 300)"/>
        <ellipse cx="250" cy="440" rx="200" ry="55" stroke-width="3.5" transform="rotate(10 250 440)"/>
        <ellipse cx="270" cy="370" rx="150" ry="120" stroke-width="3"/>
      </g>
      <g fill="none" stroke="var(--core)" stroke-opacity="0.75">
        <ellipse cx="264" cy="300" rx="230" ry="60" stroke-width="1" transform="rotate(-8 264 300)"/>
        <ellipse cx="250" cy="440" rx="200" ry="55" stroke-width="1" transform="rotate(10 250 440)"/>
        <circle cx="265" cy="368" r="78" stroke="var(--gold)" stroke-width="2" stroke-opacity="0.9"/>
      </g>
    </svg>
    <div class="vignette"></div>
    <h1 class="cover-title">
      <span class="title-the gold-text">THE</span>
      <span class="title-line gold-text">ASHES OF</span>
      <span class="title-line gold-text">CREATION</span>
    </h1>
    <p class="cover-subtitle">The Complete Vellmark Sight Trilogy</p>
    <p class="cover-author gold-text">CORWIN MALVADE</p>
  </section>

</body>
</html>
```